Harbor of Mercy - Team of Rabbis and Doctors Helping Families Dealing with Illness

The Harbor of Mercy is an organization that accompanies families dealing with severe illnesses of a family member. A team of rabbis and doctors provide support and real-time responses to these families.
The site theme is medicine and law, but the target market is religious Jewish families in crisis. Thus, the site design needs to combine:
- professional, conservative, serious
- spiritual
- warm hug

Target Market(s)

religious families suffering a health crisis

Industry/Entity Type

Non-profit organization

Number of Pages Required

1 page

Font styles to use
Sans Serif

Requirements
Must have
• Final design in PSD format. List of fonts used, colors used and link/button colors used in the design.

```html
<!DOCTYPE html>
<html lang="en">
<head>
<meta charset="utf-8">
<title>Harbor of Mercy</title>
<link href="https://fonts.googleapis.com/css2?family=Cabin:wght@500;600;700&family=Roboto:ital,wght@0,400;0,500;0,700;1,400&display=swap" rel="stylesheet">
<style>
:root{
  --blue:#1a6fc0;
  --blue-band:#2f7cbd;
  --orange:#f07a22;
  --ink:#222;
  --text:#777;
  --light:#e7f3fc;
  --footer:#1c1c1c;
  --white:#fff;
}
*{margin:0;padding:0;box-sizing:border-box}
html,body{width:1200px;height:4438px;overflow:hidden;background:var(--white)}
body{position:relative;font-family:'Roboto',sans-serif;color:var(--ink)}
.abs{position:absolute}
h1,h2,h3{font-family:'Cabin',sans-serif;font-weight:700}
.btn{position:absolute;background:var(--orange);color:#fff;border-radius:22px;font:500 14px 'Roboto',sans-serif;display:flex;align-items:center;justify-content:center;gap:8px;text-transform:uppercase}
.arrow-dot{display:inline-block;width:14px;height:14px}

/* header */
.search{left:112px;top:14px;width:306px;height:44px;background:#f0f0f0;border-radius:22px}
.search .ico{position:absolute;left:6px;top:6px;width:32px;height:32px;border-radius:50%;background:var(--blue)}
.search span{position:absolute;left:56px;top:13px;font-size:15px;color:#999}
.social{width:40px;height:40px;border-radius:50%;background:var(--orange);top:16px}
.phone-top{left:589px;top:22px;font-size:19px;font-weight:500}
.dedic{top:24px;font-size:16px;font-weight:500}
.nav{top:86px;left:112px;display:flex;font-size:15px;color:#555}
.nav a,.fnav a{color:inherit;text-decoration:none}
.logo{left:875px;top:57px;width:213px;height:84px;background:#fff;display:flex;align-items:center;justify-content:center;gap:8px;font:700 20px 'Cabin',sans-serif;color:var(--orange)}
.logo i{display:block;width:14px;height:14px;background:var(--blue)}

/* hero */
.hero{left:0;top:126px;width:1200px;height:606px;background:linear-gradient(90deg,#eeeeee 0%,#d9d9d9 40%,#6b5e57 65%,#3a302c 100%)}
.hero h1{position:absolute;left:117px;top:164px;font-size:62px;line-height:74px;color:#2a2a2a;font-weight:600}
.dot{left:62px;width:14px;height:14px;border-radius:50%;background:var(--blue)}

/* about */
.about-blue{left:112px;top:818px;width:396px;height:360px;background:var(--blue)}
.about-photo{left:186px;top:925px;width:360px;height:323px;background:#fff;padding:10px 0 0 12px}
.about-photo div{width:348px;height:313px;background:linear-gradient(135deg,#3b4a3a,#8a8560 60%,#c9b89a)}
.about h2{left:606px;top:822px;font-size:38px}
.about p{left:606px;top:878px;width:484px;font-size:14.5px;line-height:31px;color:var(--text);text-align:justify}

/* banner */
.banner{left:0;top:1331px;width:1200px;height:644px;background:radial-gradient(ellipse at 50% 60%,#a8743d 0%,#5b3820 55%,#2e1d14 100%)}
.banner h2{position:absolute;left:0;right:0;top:312px;text-align:center;color:#fff;font-size:58px;line-height:74px;font-weight:600}
.circle-arrow{width:40px;height:40px;border:2px solid #fff;border-radius:50%;top:1698px}

/* why */
.sec-title{left:0;width:1200px;text-align:center;font-size:38px}
.card{top:2130px;width:235px;height:332px;background:#fff;box-shadow:0 2px 10px rgba(0,0,0,.12);border-radius:4px;text-align:center}
.card .img{position:absolute;left:5px;top:5px;width:225px;height:160px}
.card h3{position:absolute;left:0;right:0;top:180px;font:500 15px 'Roboto',sans-serif;color:#222}
.card h3::after{content:"";display:block;width:30px;height:2px;background:var(--orange);margin:8px auto 0}
.card p{position:absolute;left:18px;right:18px;top:222px;font-size:13px;line-height:23px;color:var(--text)}
.card .more{position:absolute;left:0;right:0;top:294px;color:var(--orange);font-size:14px;font-weight:500;display:flex;justify-content:center;align-items:center;gap:8px;text-transform:uppercase}

/* testimonials */
.testi-band{left:0;top:2548px;width:1200px;height:469px;background:var(--light)}
.tcard{top:2710px;width:313px;height:229px;background:#fff;border-radius:8px;box-shadow:0 2px 10px rgba(0,0,0,.06)}
.tcard .stars{position:absolute;right:24px;top:20px;color:var(--orange);font-size:13px;letter-spacing:1px}
.tcard .q{position:absolute;left:24px;top:22px}
.tcard p{position:absolute;left:24px;right:20px;top:72px;font-style:italic;font-size:15px;line-height:26px;color:var(--text)}
.tcard .av{position:absolute;left:24px;top:164px;width:44px;height:44px;border-radius:50%;background:#6d7a66}
.tcard .name{position:absolute;left:82px;top:168px;font-size:13px;font-weight:700;text-transform:uppercase}
.tcard .role{position:absolute;left:82px;top:190px;font-size:11px;color:#888}

/* rabbi */
.rabbi{left:0;top:3017px;width:1200px;height:329px;background:var(--blue-band)}
.rabbi h2{position:absolute;left:0;right:0;top:56px;text-align:center;color:#fff;font-size:38px}
.rabbi p{position:absolute;left:180px;right:180px;top:122px;text-align:center;color:#e7f0f9;font-size:15px;line-height:26px}

/* news */
.news-main{left:112px;top:3506px;width:436px;height:346px;background:linear-gradient(135deg,#caa78c,#6e5444 60%,#3b302a)}
.news-cap{left:167px;top:3788px;width:408px;height:126px;background:#fff;border:1px solid #ddd;padding:8px}
.news-cap .inner{position:relative;border:1px solid #e5e5e5;height:108px;padding:14px 90px 0 14px}
.news-cap h3{font:700 14px 'Roboto',sans-serif;line-height:18px}
.news-cap p{font-size:11.5px;line-height:17px;color:var(--text);margin-top:6px}
.news-cap .go{position:absolute;right:0;top:0;width:58px;height:106px;background:var(--orange);display:flex;align-items:center;justify-content:center}
.ncard{left:630px;width:458px;height:191px;border:1px solid #ddd;padding:8px}
.ncard .inner{position:relative;border:1px solid #e5e5e5;height:173px}
.ncard .img{position:absolute;left:0;top:0;width:171px;height:171px}
.ncard .date{position:absolute;left:200px;top:14px;font-size:11.5px;color:var(--orange)}
.ncard h3{position:absolute;left:200px;top:42px;right:20px;font:700 15px 'Roboto',sans-serif;line-height:20px}
.ncard p{position:absolute;left:200px;top:92px;right:30px;font-size:12px;line-height:19px;color:var(--text)}
.ncard .more{position:absolute;left:200px;top:142px;font-size:12px;color:var(--orange);font-weight:500;display:flex;gap:8px;align-items:center}

/* footer */
.footer{left:0;top:4006px;width:1200px;height:432px;background:var(--footer);color:#fff}
.footer h3{position:absolute;top:76px;font:500 21px 'Roboto',sans-serif}
.footer h3::after{content:"";display:block;width:26px;height:2px;background:var(--orange);margin-top:12px}
.fitem{position:absolute;left:112px;display:flex;align-items:center;gap:18px;font-size:14px;font-weight:500}
.fico{width:28px;height:28px;border-radius:50%;background:#fff;display:flex;align-items:center;justify-content:center;flex:none}
.news-text{left:529px;top:130px;font-size:13.5px;line-height:20px;color:#ddd}
.subscribe{left:530px;top:185px;width:297px;height:42px;background:#fff;border-radius:21px;border:2px solid var(--orange)}
.subscribe span{position:absolute;left:38px;top:12px;font-size:12px;color:#888}
.subscribe b{position:absolute;right:2px;top:2px;width:110px;height:34px;border-radius:17px;background:var(--orange);font-size:12px;font-weight:500;display:flex;align-items:center;justify-content:center}
.ficon{top:148px;width:30px;height:30px;border-radius:50%;background:#fff;display:flex;align-items:center;justify-content:center}
.frule{left:112px;top:307px;width:976px;height:1px;background:#444}
.fnav{left:0;width:1200px;top:340px;display:flex;justify-content:center;font-size:14px;font-weight:500}
.copy{left:0;width:1200px;top:384px;text-align:center;font-size:13.5px}
</style>
</head>
<body>

<header>
  <div class="abs search">
    <div class="ico"><svg width="32" height="32" viewBox="0 0 32 32"><circle cx="15" cy="15" r="5" fill="none" stroke="#fff" stroke-width="2"/><line x1="19" y1="19" x2="22" y2="22" stroke="#fff" stroke-width="2"/></svg></div>
    <span>Search</span>
  </div>
  <div class="abs social" style="left:433px"></div>
  <div class="abs social" style="left:483px"><svg width="40" height="40" viewBox="0 0 40 40"><rect x="13" y="14" width="14" height="11" rx="1" fill="#fff"/><path d="M13 15l7 5 7-5" fill="none" stroke="#f07a22" stroke-width="1.4"/></svg></div>
  <div class="abs social" style="left:535px"><svg width="40" height="40" viewBox="0 0 40 40"><path d="M15 13c1-1 2-1 3 1l1 3-2 1c1 2 3 4 5 5l1-2 3 1c2 1 2 2 1 3-2 2-5 2-9-2s-4-7-3-10z" fill="#fff"/></svg></div>
  <div class="abs phone-top">+1 555 010 2040</div>
  <div class="abs dedic" style="left:802px">Dedication 1</div>
  <div class="abs dedic" style="left:927px">|</div>
  <div class="abs dedic" style="left:963px">Dedication 2</div>
  <nav class="abs nav">
    <a href="#" style="width:70px">Home</a><span style="width:30px">|</span>
    <a href="#" style="width:94px">About Us</a><span style="width:29px">|</span>
    <a href="#" style="width:115px">Why Choose Us?</a><span style="width:40px">|</span>
    <a href="#" style="width:116px">Testimonials</a><span style="width:38px">|</span>
    <a href="#" style="width:61px">News</a><span style="width:30px">|</span>
    <a href="#">Contact</a>
  </nav>
  <div class="abs logo"><i></i>Harbor of Mercy</div>
</header>

<section class="abs hero" role="img" aria-label="Father and son reading a prayer book beside lit candles">
  <h1>Should Morphine<br>Be Given To The<br>Patient?</h1>
</section>
<div class="abs dot" style="top:362px"></div>
<div class="abs dot" style="top:396px;background:#fff;border:2px solid var(--blue)"></div>
<div class="abs dot" style="top:430px"></div>

<section class="about">
  <div class="abs about-blue"></div>
  <div class="abs about-photo"><div role="img" aria-label="Rabbi holding a book with a group meeting behind him"></div></div>
  <svg class="abs" style="left:356px;top:1076px" width="30" height="30" viewBox="0 0 30 30"><circle cx="15" cy="15" r="14" fill="rgba(255,255,255,.8)"/><path d="M12 9l9 6-9 6z" fill="#555"/></svg>
  <h2 class="abs">About Us</h2>
  <p class="abs">Lorem ipsum dolor consectetur adipiscing elit, sed do eiusmod tempor incididunt ut labore et dolore magna aliqua. Ut enim ad minim veniam, quis nostrud exercitation ullamco laboris nisi ut aliquip commodo consequat. Duis aute irure dolor in reprehenderit in voluptate velit esse cillum dolore eu fugiat nulla pariatur. Excepteur sint occaecat cupidatat non proident, sunt culpa qui officia deserunt mollit animest laborum. Nostrud exercitation ullamco laboris aliquipcommodo consequat. Duis aute irure dolor in reprehenderit in voluptate velit esse cillum dolore eu fugiat nulla pariatur. Excepteur sint occaecat cupidatat non proident, sunt officia deserunt mollit anim id est laborum</p>
  <div class="btn" style="left:606px;top:1202px;width:171px;height:43px">Read More <svg class="arrow-dot" viewBox="0 0 14 14"><circle cx="7" cy="7" r="7" fill="#fff"/><path d="M5 4l3 3-3 3" fill="none" stroke="#f07a22" stroke-width="1.8"/></svg></div>
</section>

<section class="abs banner" role="img" aria-label="Grandmother and girls lighting Hanukkah candles together">
  <h2>More Moral Issues With<br>Rotating Animation</h2>
</section>
<div class="abs circle-arrow" style="left:28px"><svg width="36" height="36" viewBox="0 0 36 36"><path d="M21 11l-7 7 7 7" fill="none" stroke="#fff" stroke-width="2"/></svg></div>
<div class="abs circle-arrow" style="left:1130px"><svg width="36" height="36" viewBox="0 0 36 36"><path d="M15 11l7 7-7 7" fill="none" stroke="#fff" stroke-width="2"/></svg></div>

<h2 class="abs sec-title" style="top:2052px">Why Choose Us?</h2>
<div class="abs card" style="left:108px"><div class="img" role="img" aria-label="Teacher presenting to a class" style="background:linear-gradient(135deg,#d8d4cc,#6b6258)"></div><h3>Courses</h3><p>Lorem ipsum dolor consectetur adipiscing elit sed do eiusmod temporate incididunted.</p><div class="more">Learn More <svg class="arrow-dot" viewBox="0 0 14 14"><circle cx="7" cy="7" r="7" fill="#f07a22"/><path d="M5 4l3 3-3 3" fill="none" stroke="#fff" stroke-width="1.8"/></svg></div></div>
<div class="abs card" style="left:358px"><div class="img" role="img" aria-label="Conference room with attendees" style="background:linear-gradient(135deg,#cfcfcf,#5e5a57)"></div><h3>Conferences</h3><p>Lorem ipsum dolor consectetur adipiscing elit sed do eiusmod temporate incididunted.</p><div class="more">Learn More <svg class="arrow-dot" viewBox="0 0 14 14"><circle cx="7" cy="7" r="7" fill="#f07a22"/><path d="M5 4l3 3-3 3" fill="none" stroke="#fff" stroke-width="1.8"/></svg></div></div>
<div class="abs card" style="left:608px"><div class="img" role="img" aria-label="Lecturer speaking to a seated audience" style="background:linear-gradient(135deg,#e4e2de,#7a6f66)"></div><h3>Lectures</h3><p>Lorem ipsum dolor consectetur adipiscing elit sed do eiusmod temporate incididunted.</p><div class="more">Learn More <svg class="arrow-dot" viewBox="0 0 14 14"><circle cx="7" cy="7" r="7" fill="#f07a22"/><path d="M5 4l3 3-3 3" fill="none" stroke="#fff" stroke-width="1.8"/></svg></div></div>
<div class="abs card" style="left:856px"><div class="img" role="img" aria-label="Support agent with a headset at a desk" style="background:linear-gradient(135deg,#eeeeee,#b9aa98)"></div><h3>Hotline 24/7</h3><p>Lorem ipsum dolor consectetur adipiscing elit sed do eiusmod temporate incididunted.</p><div class="more">Learn More <svg class="arrow-dot" viewBox="0 0 14 14"><circle cx="7" cy="7" r="7" fill="#f07a22"/><path d="M5 4l3 3-3 3" fill="none" stroke="#fff" stroke-width="1.8"/></svg></div></div>

<section class="abs testi-band"></section>
<h2 class="abs sec-title" style="top:2620px">Our Testimonials</h2>
<svg class="abs" style="left:50px;top:2800px" width="22" height="24" viewBox="0 0 22 24"><path d="M14 4l-8 8 8 8" fill="none" stroke="#222" stroke-width="2"/></svg>
<svg class="abs" style="left:1128px;top:2800px" width="22" height="24" viewBox="0 0 22 24"><path d="M8 4l8 8-8 8" fill="none" stroke="#222" stroke-width="2"/></svg>
<div class="abs tcard" style="left:112px"><svg class="q" width="30" height="26" viewBox="0 0 30 26"><path d="M2 26V13C2 6 6 2 12 1v5c-3 1-4 3-4 6h4v14zM17 26V13c0-7 4-11 10-12v5c-3 1-4 3-4 6h4v14z" fill="#f07a22"/></svg><div class="stars">★★★★★</div><p>Sed uted perspiciatis uned omnis iste natus error si voluptatem accusantium doloremque laudantiumed</p><div class="av" role="img" aria-label="Reviewer portrait"></div><div class="name">Daniel Reyes</div><div class="role">Businessman</div></div>
<div class="abs tcard" style="left:443px"><svg class="q" width="30" height="26" viewBox="0 0 30 26"><path d="M2 26V13C2 6 6 2 12 1v5c-3 1-4 3-4 6h4v14zM17 26V13c0-7 4-11 10-12v5c-3 1-4 3-4 6h4v14z" fill="#f07a22"/></svg><div class="stars">★★★★★</div><p>Sed uted perspiciatis uned omnis iste natus error si voluptatem accusantium doloremque laudantiumed</p><div class="av" role="img" aria-label="Reviewer portrait"></div><div class="name">Daniel Reyes</div><div class="role">Businessman</div></div>
<div class="abs tcard" style="left:773px"><svg class="q" width="30" height="26" viewBox="0 0 30 26"><path d="M2 26V13C2 6 6 2 12 1v5c-3 1-4 3-4 6h4v14zM17 26V13c0-7 4-11 10-12v5c-3 1-4 3-4 6h4v14z" fill="#f07a22"/></svg><div class="stars">★★★★★</div><p>Sed uted perspiciatis uned omnis iste natus error si voluptatem accusantium doloremque laudantiumed</p><div class="av" role="img" aria-label="Reviewer portrait"></div><div class="name">Daniel Reyes</div><div class="role">Businessman</div></div>

<section class="abs rabbi">
  <h2>Ask The Rabbi</h2>
  <p>Lorem ipsum dolor sit amet consectetur adipiscing elit sed do eiusmod tempor incididunt ut labore et dolore magna aliqua. Ut enim ad minim veniam, quis nostrud exercitation ullamco laboris nisi ut aliquip ex ea commodo consequat. Duis aute irure dolor in reprehenderit in voluptate velit esse cillum dolore</p>
  <div class="btn" style="left:515px;top:227px;width:169px;height:42px">Contact Us <svg class="arrow-dot" viewBox="0 0 14 14"><circle cx="7" cy="7" r="7" fill="#fff"/><path d="M5 4l3 3-3 3" fill="none" stroke="#f07a22" stroke-width="1.8"/></svg></div>
</section>

<h2 class="abs sec-title" style="top:3419px">Latest News</h2>
<div class="abs news-main" role="img" aria-label="Father reading a book with his three daughters"></div>
<div class="abs news-cap"><div class="inner"><h3>Lorem ipsum dolor sit amet, consectetur adipiscing elit</h3><p>Sed ut perspiciatis unde omnis iste natus error sit voluptatem accusantium doloremque</p><div class="go"><svg width="24" height="24" viewBox="0 0 24 24"><circle cx="12" cy="12" r="12" fill="#fff"/><path d="M10 7l5 5-5 5" fill="none" stroke="#f07a22" stroke-width="2.4"/></svg></div></div></div>
<div class="abs ncard" style="top:3506px"><div class="inner"><div class="img" role="img" aria-label="Woman reading beside bookshelves" style="background:linear-gradient(135deg,#e8e2d8,#6a4c3c)"></div><div class="date">▣ Dec 12 , 2023</div><h3>Lorem ipsum dolor sit amet, consectetur</h3><p>Sed ut perspiciatis unde omnis iste natus error sit voluptatem</p><div class="more">READ MORE <svg width="12" height="12" viewBox="0 0 14 14"><circle cx="7" cy="7" r="7" fill="#f07a22"/><path d="M5 4l3 3-3 3" fill="none" stroke="#fff" stroke-width="1.8"/></svg></div></div></div>
<div class="abs ncard" style="top:3723px"><div class="inner"><div class="img" role="img" aria-label="Mother reading with her children" style="background:linear-gradient(135deg,#c9b8a6,#2a2422)"></div><div class="date">▣ Dec 12 , 2023</div><h3>Lorem ipsum dolor sit amet, consectetur</h3><p>Sed ut perspiciatis unde omnis iste natus error sit voluptatem</p><div class="more">READ MORE <svg width="12" height="12" viewBox="0 0 14 14"><circle cx="7" cy="7" r="7" fill="#f07a22"/><path d="M5 4l3 3-3 3" fill="none" stroke="#fff" stroke-width="1.8"/></svg></div></div></div>

<footer class="abs footer">
  <h3 style="left:112px">Address</h3>
  <h3 style="left:529px">Subscribe Newsletter</h3>
  <h3 style="left:964px">Follow Us On</h3>
  <div class="fitem" style="top:140px;height:40px"><span class="fico"><svg width="14" height="16" viewBox="0 0 14 16"><path d="M7 1a5 5 0 0 1 5 5c0 4-5 9-5 9S2 10 2 6a5 5 0 0 1 5-5z" fill="#f07a22"/><circle cx="7" cy="6" r="2" fill="#fff"/></svg></span><span style="line-height:20px">PO Box 142, Lorem ipsum dolor<br>sit amet United States</span></div>
  <div class="fitem" style="top:196px;height:28px;font-size:17px"><span class="fico"><svg width="14" height="14" viewBox="0 0 14 14"><path d="M2 1c1-1 2-1 3 1l1 2-2 1c1 2 2 3 4 4l1-2 2 1c2 1 2 2 1 3-2 2-4 2-7-1S1 3 2 1z" fill="#f07a22"/></svg></span>+ 1 555 010 2040</div>
  <div class="fitem" style="top:251px;height:28px"><span class="fico"><svg width="14" height="12" viewBox="0 0 14 12"><rect x="0" y="1" width="14" height="10" rx="1" fill="#f07a22"/><path d="M0 2l7 5 7-5" fill="none" stroke="#fff" stroke-width="1.2"/></svg></span>info@harborofmercy.org</div>
  <p class="abs news-text">Lorem ipsum dolor sit amet, consectetur<br>adipiscing elit, sed do eiusmod</p>
  <div class="abs subscribe"><svg class="abs" style="left:18px;top:15px" width="12" height="10" viewBox="0 0 14 12"><rect x="0" y="1" width="14" height="10" rx="1" fill="#777"/><path d="M0 2l7 5 7-5" fill="none" stroke="#fff" stroke-width="1.2"/></svg><span>Email Address *</span><b>SUBSCRIBE</b></div>
  <div class="abs ficon" style="left:966px"></div>
  <div class="abs ficon" style="left:1008px"><svg width="14" height="12" viewBox="0 0 14 12"><rect x="0" y="1" width="14" height="10" rx="1" fill="#1a6fc0"/><path d="M0 2l7 5 7-5" fill="none" stroke="#fff" stroke-width="1.2"/></svg></div>
  <div class="abs frule"></div>
  <nav class="abs fnav">
    <a href="#">Home</a><span style="margin:0 28px">|</span>
    <a href="#">About Us</a><span style="margin:0 28px">|</span>
    <a href="#">Why Choose Us?</a><span style="margin:0 38px">|</span>
    <a href="#">Testimonials</a><span style="margin:0 38px">|</span>
    <a href="#">News</a><span style="margin:0 28px">|</span>
    <a href="#">Contact</a>
  </nav>
  <p class="abs copy">© 2023 Harbor of Mercy. All Rights Reserved</p>
</footer>

</body>
</html>
```